Cradlecraft by Lorna Business Card Design

i am starting a new business as a reborn artist (that is painting dolls to make them look like real live babies)

i eventually want to sell the dolls that i make and have classed in reborning. but at the moment i just want to get my name out there.

I do not currently have images of the dolls so cannot have an image in the design.

Non compulsory thoughts: i like the look of old wood, white and baby pink,even hot pink, and lace, denim. i had in mind something like a tiny baby in a old cradle or something, a old drawer, box, something different or unusual, it has to be a girl baby. i am also open to other thoughts on the matter. i would like plain writing not all swirly
Updates

Sorry to change but would like it to read country cradlecraft by lorna.

Industry/Entity Type

Painting

Contact Information for Business Card

Cradlecraft by Lorna
little treasures painted by hand
Reborn Artist Lorna Whitby
0431 756 842
marlo.t@quillbox.com

```html
<!DOCTYPE html>
<html lang="en">
<head>
<meta charset="utf-8">
<title>Cradlecraft by Lorna – Business Card</title>
<link rel="stylesheet" href="https://fonts.googleapis.com/css2?family=Quicksand:wght@300;400&display=swap">
<style>
  :root {
    --wood-light: #74624f;
    --wood-mid: #65533f;
    --wood-dark: #54442f;
    --text-main: #ffffff;
    --text-soft: #ece4da;
    --text-shadow: rgba(30, 20, 12, 0.55);
  }
  html, body {
    margin: 0;
    padding: 0;
    width: 1200px;
    height: 741px;
    overflow: hidden;
    background: var(--wood-mid);
  }
  .card {
    position: relative;
    width: 1200px;
    height: 741px;
    overflow: hidden;
    font-family: "Quicksand", sans-serif;
    color: var(--text-main);
  }
  .card__wood {
    position: absolute;
    inset: 0;
    background: linear-gradient(180deg, var(--wood-light) 0%, var(--wood-mid) 45%, var(--wood-dark) 100%);
  }
  .card__text {
    position: absolute;
    left: 0;
    width: 100%;
    margin: 0;
    text-align: center;
    line-height: 1;
    text-shadow: 1px 2px 3px var(--text-shadow);
    white-space: nowrap;
  }
  .brand-title {
    top: 108px;
    font-size: 104px;
    font-weight: 400;
    letter-spacing: 1px;
  }
  .brand-byline {
    top: 248px;
    font-size: 66px;
    font-weight: 400;
    letter-spacing: 1px;
  }
  .tagline {
    top: 354px;
    font-size: 50px;
    font-weight: 300;
    color: var(--text-soft);
    letter-spacing: 1px;
  }
  .contact {
    font-size: 36px;
    font-weight: 300;
    color: var(--text-soft);
  }
  .contact--role { top: 430px; }
  .contact--name { top: 485px; }
  .contact--phone { top: 540px; }
  .contact--email { top: 594px; }
</style>
</head>
<body>
  <main class="card">
    <div class="card__wood" role="img" aria-label="Weathered brown wood grain background"></div>
    <h1 class="card__text brand-title">Cradlecraft</h1>
    <p class="card__text brand-byline">by Lorna</p>
    <p class="card__text tagline">little treasures painted by hand</p>
    <p class="card__text contact contact--role">Reborn Artist</p>
    <p class="card__text contact contact--name">Lorna Whitby</p>
    <p class="card__text contact contact--phone">0431-756-842</p>
    <p class="card__text contact contact--email">marlo.t@quillbox.com</p>
  </main>
</body>
</html>
```